Simple Business Cards for Self-employed Coach

Simple business card with a design that includes the QLT logo.
Using either only the logo color or additional colors that match the logo.

Meridian Guides reach deeply into the past, gathering wisdom from East and West, while still staying current with the frontiers of new discovery in cognitive science, genetics, and other disciplines. see https://www.brightharborpath.example/what-is-integral-coaching/

Target Market(s)

Coaching Clients in Tokyo /Asia; in business organizations, but also outside

Industry/Entity Type

Life Coaching

Contact Information for Business Card

Lukas Brenning
Certified Meridian Guide

3-2-48 Kamiyoshi
Nakarino 164-0392
Tokyo, Japan

Phone: +81 70 4817 5062
E-Mail: lukas.brenning@mailora.example

Font styles to use
Sans Serif

Colors
00a990

Requirements
Must have
• include uploaded logo
• color fitting with QLT logo color
Nice to have
• simple, elegant design
Should not have
• clutter

```html
<!DOCTYPE html>
<html lang="en">
<head>
<meta charset="utf-8">
<title>Lukas Brenning – Business Card</title>
<link rel="stylesheet" href="https://fonts.googleapis.com/css2?family=Arimo:wght@400;700&family=Roboto+Condensed:wght@300;400&display=swap">
<style>
  :root {
    --teal: #00a990;
    --teal-deep: #007a67;
    --ink: #1c1b1c;
    --paper: #ffffff;
    --backdrop: #2a2a2a;
  }
  html, body {
    margin: 0;
    padding: 0;
    width: 1200px;
    height: 1200px;
    overflow: hidden;
    background: var(--backdrop);
  }
  .stage {
    position: relative;
    width: 1200px;
    height: 1200px;
  }
  .card {
    position: absolute;
    left: 100px;
    top: 315px;
    width: 1000px;
    height: 570px;
    background: var(--paper);
    overflow: hidden;
    font-family: "Arimo", Arial, sans-serif;
  }
  .brand {
    position: absolute;
    left: 62px;
    top: 58px;
    display: flex;
    align-items: center;
    gap: 16px;
  }
  .brand-square {
    width: 44px;
    height: 44px;
    background: var(--teal);
  }
  .brand-name {
    font-weight: 700;
    font-size: 52px;
    letter-spacing: 10px;
    color: var(--teal);
    line-height: 1;
  }
  .name-band {
    position: absolute;
    left: 0;
    top: 255px;
    width: 600px;
    height: 122px;
    background: var(--ink);
    color: var(--paper);
  }
  .person-name {
    position: absolute;
    left: 62px;
    top: 26px;
    margin: 0;
    font-weight: 700;
    font-size: 38px;
    letter-spacing: 2px;
    text-transform: uppercase;
  }
  .person-title {
    position: absolute;
    left: 64px;
    top: 72px;
    margin: 0;
    font-family: "Roboto Condensed", "Arial Narrow", sans-serif;
    font-weight: 300;
    font-size: 30px;
  }
  .contact {
    position: absolute;
    left: 62px;
    top: 410px;
    margin: 0;
    font-weight: 700;
    font-size: 25px;
    line-height: 1.45;
    color: var(--ink);
  }
  .address-block {
    position: absolute;
    left: 590px;
    top: 215px;
    right: 0;
    bottom: 0;
    background: radial-gradient(ellipse at 45% 40%, var(--teal) 0%, #009a83 55%, var(--teal-deep) 100%);
  }
  .address {
    position: absolute;
    right: 48px;
    bottom: 40px;
    margin: 0;
    font-style: normal;
    font-weight: 700;
    font-size: 33px;
    line-height: 1.25;
    text-align: right;
    color: var(--paper);
  }
</style>
</head>
<body>
  <div class="stage">
    <article class="card">
      <div class="brand">
        <span class="brand-square"></span>
        <span class="brand-name">QLT</span>
      </div>

      <div class="name-band">
        <h1 class="person-name">Lukas Brenning</h1>
        <p class="person-title">Certified Meridian Guide</p>
      </div>

      <p class="contact">
        Phone: +81 70 4817 5062<br>
        E-Mail: lukas.brenning@mailora.example
      </p>

      <div class="address-block">
        <address class="address">
          3-2-48 Kamiyoshi<br>
          Nakarino 164-0392<br>
          Tokyo, Japan
        </address>
      </div>
    </article>
  </div>
</body>
</html>
```